Lumen Homes Recruitment (Social Media)

REAL ESTATE AGENTS WANTED
LUMEN HOMES CEDAR QUAY

*Competitive Commission Splits
*Residual Income for Recruitment
*Virtual Training & Development
*Investment Club for Agents & Clients

Call us today at (800) 482-3957
or email us for more information at info@LumenHomesCedarQuay.example

482 Birchmont Court, Suite 210, Fallow Creek, MD 20913
www.LumenHomesCedarQuay.example

Requirements
Must have
• 16 x 16 print size
African American Images

```html
<!DOCTYPE html>
<html lang="en">
<head>
<meta charset="utf-8">
<title>Lumen Homes – Real Estate Agents Wanted</title>
<link href="https://fonts.googleapis.com/css2?family=Montserrat:wght@500;600;700;800;900&display=swap" rel="stylesheet">
<style>
  :root {
    --teal: #17919c;
    --teal-dark: #117a84;
    --orange: #e9582a;
    --ink: #1d1d1f;
    --paper: #ffffff;
    --backdrop: #e8e4da;
    --photo-sky: #c9cfd2;
    --photo-house: #b9aea3;
    --photo-ground: #8e8a84;
    --rule: #cfcfcf;
  }
  * { box-sizing: border-box; margin: 0; padding: 0; }
  html, body { width: 1200px; height: 1200px; overflow: hidden; }
  body {
    background: var(--backdrop);
    font-family: "Montserrat", sans-serif;
    color: var(--ink);
  }
  .flyer {
    position: absolute;
    left: 200px; top: 40px;
    width: 800px; height: 1120px;
    background: var(--paper);
    overflow: hidden;
  }
  .hero-photo {
    position: absolute;
    left: 0; top: 200px; width: 800px; height: 540px;
    background: linear-gradient(180deg, var(--photo-sky) 0%, var(--photo-house) 45%, #a99b8c 70%, var(--photo-ground) 100%);
  }
  .header-band, .lower-panel { position: absolute; left: 0; width: 800px; }
  .header-band { top: 0; height: 420px; }
  .lower-panel { top: 560px; height: 560px; }
  .headline {
    position: absolute; left: 0; top: 60px; width: 800px;
    text-align: center; color: #fff;
  }
  .ribbon {
    display: inline-block;
    background: var(--orange);
    color: #fff;
    font-weight: 700; font-size: 30px; letter-spacing: 7px;
    padding: 8px 34px 8px 40px;
    clip-path: polygon(0 0, 100% 0, 96% 50%, 100% 100%, 0 100%, 4% 50%);
  }
  .headline-main {
    font-weight: 900; font-size: 108px; line-height: 0.95;
    letter-spacing: -1px; margin-top: 6px;
  }
  .benefits {
    position: absolute; left: 70px; top: 700px; width: 680px;
    display: grid; grid-template-columns: 320px 340px; row-gap: 30px; column-gap: 20px;
    list-style: none;
  }
  .benefit {
    display: flex; gap: 10px; align-items: flex-start;
    font-weight: 600; font-size: 23px; line-height: 1.22;
  }
  .benefit svg { flex: none; margin-top: 2px; }
  .brand {
    position: absolute; left: 30px; top: 930px; width: 210px;
    display: flex; align-items: center; gap: 10px;
  }
  .brand-mark { width: 28px; height: 28px; background: var(--teal); flex: none; }
  .brand-name { font-weight: 800; font-size: 20px; line-height: 1.12; color: var(--teal-dark); }
  .contact {
    position: absolute; left: 250px; top: 870px; width: 320px;
    list-style: none;
  }
  .contact li {
    display: flex; align-items: center; gap: 8px;
    padding: 6px 0; border-bottom: 1px dashed var(--rule);
    white-space: nowrap;
  }
  .contact li:last-child { border-bottom: none; align-items: flex-start; }
  .contact-phone { font-weight: 700; font-size: 31px; }
  .contact-small { font-weight: 500; font-size: 12.5px; line-height: 1.35; }
  .join-callout {
    position: absolute; left: 590px; top: 850px; width: 210px; height: 190px;
    background: var(--orange); color: #fff;
    font-weight: 700; font-size: 27px; line-height: 1.15;
    padding: 28px 22px;
  }
  .footer-band {
    position: absolute; left: 0; top: 1040px; width: 800px; height: 80px;
    background: var(--teal); color: #fff;
    font-weight: 700; font-size: 23px;
    display: flex; align-items: center; justify-content: center;
  }
</style>
</head>
<body>
<main class="flyer">
  <div class="hero-photo" role="img" aria-label="Photo of a family looking at their new house while an agent hangs a red SOLD sign"></div>

  <svg class="header-band" viewBox="0 0 800 420" aria-hidden="true">
    <path d="M0 0 H800 V270 Q520 380 0 400 Z" fill="var(--teal)"/>
  </svg>

  <header class="headline">
    <div class="ribbon">REAL ESTATE</div>
    <h1 class="headline-main">AGENTS<br>WANTED</h1>
  </header>

  <svg class="lower-panel" viewBox="0 0 800 560" aria-hidden="true">
    <path d="M0 120 Q300 20 800 40 V560 H0 Z" fill="var(--paper)"/>
    <path d="M0 120 Q300 20 800 40" fill="none" stroke="var(--orange)" stroke-width="5"/>
  </svg>

  <ul class="benefits">
    <li class="benefit"><svg width="24" height="24" viewBox="0 0 24 24"><circle cx="12" cy="12" r="12" fill="var(--teal)"/><path d="M6.5 12.5 10.5 16 17.5 8" fill="none" stroke="#fff" stroke-width="2.6"/></svg><span>Competitive<br>Commission Splits</span></li>
    <li class="benefit"><svg width="24" height="24" viewBox="0 0 24 24"><circle cx="12" cy="12" r="12" fill="var(--teal)"/><path d="M6.5 12.5 10.5 16 17.5 8" fill="none" stroke="#fff" stroke-width="2.6"/></svg><span>Virtual Training<br>&amp; Development</span></li>
    <li class="benefit"><svg width="24" height="24" viewBox="0 0 24 24"><circle cx="12" cy="12" r="12" fill="var(--teal)"/><path d="M6.5 12.5 10.5 16 17.5 8" fill="none" stroke="#fff" stroke-width="2.6"/></svg><span>Residual Income<br>for Recruitment</span></li>
    <li class="benefit"><svg width="24" height="24" viewBox="0 0 24 24"><circle cx="12" cy="12" r="12" fill="var(--teal)"/><path d="M6.5 12.5 10.5 16 17.5 8" fill="none" stroke="#fff" stroke-width="2.6"/></svg><span>Investment Club<br>for Agents &amp; Clients</span></li>
  </ul>

  <div class="brand">
    <span class="brand-mark"></span>
    <span class="brand-name">LUMEN HOMES CEDAR QUAY</span>
  </div>

  <ul class="contact">
    <li>
      <svg width="24" height="24" viewBox="0 0 24 24"><path d="M6 2 9 2 11 7 8.5 9a12 12 0 0 0 6.5 6.5L17 13l5 2v3a3 3 0 0 1-3 3A17 17 0 0 1 3 5a3 3 0 0 1 3-3Z" fill="var(--orange)"/></svg>
      <span class="contact-phone">(800) 482-3957</span>
    </li>
    <li>
      <svg width="14" height="10" viewBox="0 0 14 10"><rect width="14" height="10" fill="var(--orange)"/><path d="M0 0 7 6 14 0" fill="none" stroke="#fff" stroke-width="1.3"/></svg>
      <span class="contact-small">info@LumenHomesCedarQuay.example</span>
    </li>
    <li>
      <svg width="12" height="16" viewBox="0 0 12 16"><path d="M6 0a6 6 0 0 1 6 6c0 4-6 10-6 10S0 10 0 6a6 6 0 0 1 6-6Z" fill="var(--orange)"/><circle cx="6" cy="6" r="2.2" fill="#fff"/></svg>
      <span class="contact-small">482 Birchmont Court, Suite 210,<br>Fallow Creek, MD 20913</span>
    </li>
  </ul>

  <div class="join-callout">CALL OR<br>EMAIL TO<br>JOIN OUR<br>TEAM</div>

  <footer class="footer-band">www.LumenHomesCedarQuay.example</footer>
</main>
</body>
</html>
```